automotive repair and collision repair shop card

our company is called K.W Motor service we are a automotive repair company
we also do government inspections. the company information is on the cards. I would like you to use my new logo and create a new card and use the information from my old card. Good Luck!!

Industry/Entity Type

Car Repair

Contact Information for Business Card

Address: #417-10952 58 Ave, Surrey, BC V3X 4K8
Phone:(604) 555-0178
fax 604 555 0193
website www.kwmotorworks.example

Font styles to use
Serif
Sans Serif

Requirements
Must have
• all the information
Should not have
• the owner and there name

```html
<!DOCTYPE html>
<html lang="en">
<head>
<meta charset="utf-8">
<title>K.W Motor service – Business Card</title>
<link href="https://fonts.googleapis.com/css2?family=Oswald:wght@400&family=Roboto+Condensed:wght@400;700&family=Pathway+Gothic+One&display=swap" rel="stylesheet">
<style>
  :root {
    --backdrop: #d9d9d6;
    --card: #f4f3f0;
    --ink: #2b2b2b;
    --ink-soft: #4a4a4a;
    --rule: #3a3a3a;
  }
  * { box-sizing: border-box; margin: 0; padding: 0; }
  html, body {
    width: 1200px;
    height: 873px;
    overflow: hidden;
    background: var(--backdrop);
  }
  .canvas {
    position: relative;
    width: 1200px;
    height: 873px;
    display: flex;
    align-items: center;
    justify-content: center;
  }
  .business-card {
    position: relative;
    width: 900px;
    height: 514px;
    background: var(--card);
    color: var(--ink);
    box-shadow: 0 6px 18px rgba(0,0,0,0.18);
  }
  .contact-list {
    position: absolute;
    top: 38px;
    left: 48px;
    list-style: none;
    font-family: "Roboto Condensed", Arial, sans-serif;
    font-size: 17px;
    line-height: 1.3;
    color: var(--ink-soft);
  }
  .contact-list .label {
    display: inline-block;
    width: 18px;
    font-weight: 700;
    color: var(--ink);
  }
  .brand-rule {
    position: absolute;
    top: 250px;
    left: 48px;
    width: 690px;
    height: 2px;
    background: var(--rule);
  }
  .brand-name {
    position: absolute;
    top: 254px;
    left: 48px;
    font-family: "Oswald", "Arial Narrow", sans-serif;
    font-weight: 400;
    font-size: 84px;
    line-height: 1.1;
    letter-spacing: 1px;
    color: var(--ink);
    white-space: nowrap;
  }
  .tagline {
    position: absolute;
    top: 360px;
    left: 430px;
    font-family: "Pathway Gothic One", "Arial Narrow", sans-serif;
    font-size: 30px;
    color: var(--ink);
  }
  .service-list {
    position: absolute;
    top: 318px;
    right: 40px;
    list-style: none;
    font-family: "Roboto Condensed", Arial, sans-serif;
    font-size: 16px;
    line-height: 1.25;
    color: var(--ink-soft);
  }
  .service-list li::before {
    content: "";
    display: inline-block;
    width: 5px;
    height: 5px;
    margin: 0 7px 2px 0;
    border-radius: 50%;
    background: var(--ink);
  }
</style>
</head>
<body>
  <main class="canvas">
    <article class="business-card">
      <ul class="contact-list">
        <li><span class="label">A</span>#417-10952 58 Ave, Surrey, BC V3X 4K8</li>
        <li><span class="label">P</span>(604) 555-0178</li>
        <li><span class="label">F</span>604 555 0193</li>
        <li><span class="label">W</span>www.kwmotorworks.example</li>
      </ul>

      <div class="brand-rule"></div>
      <h1 class="brand-name">K.W Motor service</h1>
      <p class="tagline">One Stop Repair Shop</p>

      <ul class="service-list">
        <li>Oil change</li>
        <li>Scheduled maintenance</li>
        <li>Body Work</li>
        <li>Paint</li>
        <li>Glass Replacement</li>
        <li>PVIC Claims</li>
        <li>Inspections</li>
        <li>Engine repair</li>
      </ul>
    </article>
  </main>
</body>
</html>
```